Flu Brochure- brief and easy-to-read

A team of health educators is looking to design a brochure on what Americans need to "know and do" when it comes to flu season. All copy and images will be provided.

The brochure needs to be an 8.5 x 11 inch bi-fold design.

I am only able to upload up to 5 files. So, additional images will have to sent via dropbox or some other mechanism.

Target Market(s)

The audience is vast, but the content and design need to be simple and engaging.

Industry/Entity Type

Health

Requirements
Must have
• Must Have:
- Clear and Simple, Easy-to-read and Understand and Act on- should be very focused on what the consumer should do about taking care of themselves when it comes to the flu.

We will provide all of the copy for the brochure design. We will also provide photographs for the project.

Captions for photographs that support the key message.

Should Not Have:
- x reverse print- e.g., no white font on a black background
x fancy fonts or heavy use of italics
x use of all capitals
x no full justification
x no use of drop caps

Must be multicultural as well.

```html
<!DOCTYPE html>
<html lang="en">
<head>
<meta charset="utf-8">
<title>Flu Season Brochure – Know, Prevent, Protect</title>
<link rel="stylesheet" href="https://fonts.googleapis.com/css2?family=Varela+Round&family=Open+Sans:wght@400;600&display=swap">
<style>
  :root {
    --canvas: #ecebe8;
    --sky: #16a6e6;
    --sky-pale: #cfeaf9;
    --navy: #1d3e8e;
    --orange: #f15a29;
    --paper: #ffffff;
    --phone-red: #e8403a;
    --photo-clinic: #b9b3ad;
    --photo-water: #d9dde0;
  }
  * { box-sizing: border-box; margin: 0; padding: 0; }
  html, body { width: 1200px; height: 1000px; overflow: hidden; }
  body { background: var(--canvas); font-family: "Open Sans", Arial, sans-serif; color: var(--navy); }

  .spread { position: absolute; left: 60px; top: 70px; width: 1080px; height: 860px; box-shadow: 0 6px 24px rgba(0,0,0,.18); }
  .page { position: absolute; top: 0; width: 540px; height: 860px; overflow: hidden; }
  .page--left { left: 0; background: var(--sky); }
  .page--right { left: 540px; background: var(--paper); }

  .tab { position: absolute; height: 42px; padding: 0 26px 0 18px; background: var(--sky-pale);
         border-radius: 0 10px 0 0; font-family: "Varela Round", Arial, sans-serif; font-size: 28px;
         color: var(--navy); display: flex; align-items: center; gap: 18px; z-index: 2; }
  .tab__num { font-weight: 700; font-size: 24px; }

  .panel { position: absolute; background: var(--paper); }
  .panel--facts { left: 20px; top: 130px; width: 490px; height: 300px; border-radius: 0 40px 40px 0; padding: 22px 28px; }
  .panel--signs { left: 40px; top: 460px; width: 480px; height: 370px; border-radius: 24px; padding: 26px 30px; }

  .lead { font-family: "Varela Round", Arial, sans-serif; color: var(--orange); font-size: 30px; font-weight: 400; margin-bottom: 14px; }
  .body-copy { font-size: 16.5px; line-height: 1.3; }
  .body-copy p { margin-bottom: 9px; }
  .kicker { color: var(--orange); }
  .kicker--indent { margin-left: 22px; margin-top: 14px; }
  .indent { margin-left: 22px; }

  .bubble { position: absolute; left: 140px; top: 220px; width: 190px; padding: 10px 12px; border: 3px solid var(--orange);
            border-radius: 20px; background: var(--paper); color: var(--orange); font-size: 16.5px; line-height: 1.25; text-align: center; }
  .bubble__tail { position: absolute; left: 244px; top: 302px; }
  .phone-photo { position: absolute; left: 300px; top: 280px; width: 150px; height: 90px; border-radius: 40px 40px 18px 18px;
                 background: radial-gradient(circle at 45% 35%, #f06a60, var(--phone-red) 60%, #b52b26); }

  .blue-strip { position: absolute; left: 0; width: 540px; background: var(--sky); }
  .photo-clinic { position: absolute; right: 0; top: 0; width: 190px; height: 300px; border-radius: 0 0 0 36px;
                  background: linear-gradient(160deg, #e7e3df, var(--photo-clinic) 55%, #3f8f6f); z-index: 1; }
  .prevent { position: absolute; left: 22px; top: 116px; width: 310px; }
  .question { color: var(--orange); font-size: 16.5px; line-height: 1.25; margin-bottom: 8px; }
  .shot-list { position: absolute; left: 22px; top: 300px; width: 480px; font-size: 16.5px; line-height: 1.3; }
  .shot-list ul { list-style: none; margin-left: 12px; }
  .shot-list li::before { content: "- "; }

  .protect { position: absolute; left: 22px; top: 452px; width: 500px; }
  .steps { list-style: none; }
  .steps li { position: relative; padding-left: 26px; margin-bottom: 6px; font-size: 16.5px; line-height: 1.3; }
  .steps li svg { position: absolute; left: 2px; top: 6px; }
  .photo-wash { position: absolute; left: 40px; top: 672px; width: 500px; height: 188px; border-radius: 28px 0 0 0;
                background: linear-gradient(135deg, #c4cacf, var(--photo-water) 45%, #f1d9cf); }
</style>
</head>
<body>
<main class="spread">

  <section class="page page--left">
    <div class="tab" style="left:20px; top:88px;"><span class="tab__num">1</span>Know</div>
    <div class="panel panel--facts">
      <h2 class="lead">... the facts:</h2>
      <div class="body-copy">
        <p>The flu is a virus.<br>If you get the flu, you may not feel that bad, but sometimes the flu can make you so sick that you can die.</p>
        <p>You catch flu from other people.</p>
        <p>People with flu spread it by coughing, sneezing, or spreading their germs.</p>
      </div>
    </div>

    <div class="panel panel--signs">
      <div class="body-copy">
        <p class="kicker">Know - common complaints for flu:</p>
        <p>fever, cough, sore throat, runny or stuffy nose, headaches, body aches, chills, being tired</p>
        <p class="kicker kicker--indent">Know - the warning signs:</p>
        <p class="indent">hard time breathing or short of breath<br>pain or pressure in the chest or stomach<br>feeling dizzy all of a sudden becoming confused</p>
      </div>
      <p class="bubble">If you have ANY of the warning signs, contact your doctor!</p>
      <svg class="bubble__tail" width="40" height="34" viewBox="0 0 40 34" aria-hidden="true">
        <path d="M2 0 L30 30 L22 0" fill="#fff" stroke="#f15a29" stroke-width="3" stroke-linejoin="round"/>
      </svg>
      <div class="phone-photo" role="img" aria-label="Photo of a red rotary telephone"></div>
    </div>
  </section>

  <section class="page page--right">
    <div class="blue-strip" style="top:0; height:100px;"></div>
    <div class="photo-clinic" role="img" aria-label="Photo of a nurse in green scrubs giving a child a nasal spray flu vaccine"></div>
    <div class="tab" style="left:10px; top:62px;"><span class="tab__num">2</span>Prevent</div>

    <div class="prevent body-copy">
      <p class="question">How Can I Keep Me And My Family From Getting Flu?</p>
      <p>Be sure everyone 6 months and older gets a flu shot. You can get a flu shot through a needle or a spray.</p>
      <p>The flu shot helps protect you against the three most common types of flu.</p>
    </div>
    <div class="shot-list">
      <p>The shot...</p>
      <ul>
        <li>does not give you the flu</li>
        <li>is very important for pregnant women, and</li>
        <li>you don't need a prescription for it!</li>
      </ul>
    </div>

    <div class="blue-strip" style="top:396px; height:14px;"></div>
    <div class="tab" style="left:10px; top:404px;"><span class="tab__num">3</span>Protect</div>

    <div class="protect">
      <p class="question">How Do I Protect My Family?</p>
      <ul class="steps">
        <li><svg width="10" height="12" viewBox="0 0 10 12" aria-hidden="true"><path d="M2 1 L8 6 L2 11" fill="none" stroke="#1d3e8e" stroke-width="2.5"/></svg>Stay away from sick people.</li>
        <li><svg width="10" height="12" viewBox="0 0 10 12" aria-hidden="true"><path d="M2 1 L8 6 L2 11" fill="none" stroke="#1d3e8e" stroke-width="2.5"/></svg>Wash your hands with soap and water or hand sanitizer when you eat, cough or go to the bathroom.</li>
        <li><svg width="10" height="12" viewBox="0 0 10 12" aria-hidden="true"><path d="M2 1 L8 6 L2 11" fill="none" stroke="#1d3e8e" stroke-width="2.5"/></svg>Try not to touch your eyes, nose or mouth because that is how you catch flu.</li>
        <li><svg width="10" height="12" viewBox="0 0 10 12" aria-hidden="true"><path d="M2 1 L8 6 L2 11" fill="none" stroke="#1d3e8e" stroke-width="2.5"/></svg>Cough or sneeze into your sleeve or cover your nose and mouth with a tissue. Throw the tissue in the trash!</li>
      </ul>
    </div>

    <div class="blue-strip" style="top:700px; height:160px; width:40px;"></div>
    <div class="photo-wash" role="img" aria-label="Photo of soapy hands being washed under running water"></div>
  </section>

</main>
</body>
</html>
```